Flyer Design

I need a flyer design for a new company based in Scotland called Snapwell Mite solution,s we want to provide a service power washing wheelie bins for the hotel and catering trade and domestic wheelie bins.We want a flyer with a few animated germs and Snapwell on the front we want to make out that by touching this flyer or the bin you may have come in contact with harmful germs including salmonella ecoli influenza and that you could potentially contaminate anything else you may touch including other people or risk cross contamination by spreading the germs to door handles etc.We also want a section of the flyer where clients can register their bins for cleaning.We need a basic registration form where our clients can write their postcode establishment name or house number.what day their bins are emptied.Our crew will follow the waste disposal vehicle and clean the bin when empty.The flyer should inform the client that a 4 wheele bin (dumpster) costs £10 for the first clean and £5 per subsequent clean and a 2 wheele bin (wheelie) costs £6 for the first clean and £3 per subsequent clean.The flyer should inform the client that they may register by texting their information to 07912448731.eg KT37QB the pub Black dumpster Tuesday.
Updates

The address and post code in original brief haven't to go on flyer and only Snapwell and the germ representation to be on the front of the flyer on the bottom 2 thirds as the top o As the top part will be under thr bin lid thanks Ewan.

Industry/Entity Type

Catering

Requirements
Must have
• The flyer must have only Snapwell and the germ logo on the front of the flyer.
The postcode and address from the brief hasn't to go on the flyer.
Nice to have
• A logo that's serious but jot frightening.

```html
<!DOCTYPE html>
<html lang="en">
<head>
<meta charset="utf-8">
<title>Snapwell Mite Solutions – Bin Cleaning Flyer</title>
<link rel="stylesheet" href="https://fonts.googleapis.com/css2?family=Barlow+Condensed:wght@700&family=Rubik:wght@300;400;700&family=Roboto:wght@300;400;700&display=swap">
<style>
  :root {
    --page-bg: #dedede;
    --night: #0b0f17;
    --white: #ffffff;
    --cyan: #4fc6f0;
    --lime: #9cf01c;
    --lime-text: #8ee84a;
    --salmon: #f4a070;
    --ink: #1a1a1a;
    --grey-text: #7a7a7a;
    --form-band: #e2fbc9;
    --field: #ffffff;
  }
  * { margin: 0; padding: 0; box-sizing: border-box; }
  html, body { width: 1200px; height: 1000px; overflow: hidden; }
  body { background: var(--page-bg); position: relative; font-family: "Roboto", Arial, sans-serif; }

  .flyer { position: absolute; overflow: hidden; }

  /* Front */
  .flyer-front {
    left: 48px; top: 107px; width: 548px; height: 776px;
    background:
      radial-gradient(ellipse 330px 170px at 470px 700px, rgba(255,255,255,0.95) 0%, rgba(220,235,245,0.7) 35%, rgba(40,80,120,0.35) 70%, rgba(11,15,23,0) 100%),
      var(--night);
  }
  .germ-photo {
    position: absolute; left: 0; top: 0; width: 548px; height: 380px;
    background:
      radial-gradient(ellipse at 30% 40%, #b0723d 0%, rgba(176,114,61,0) 45%),
      radial-gradient(ellipse at 75% 30%, #3fa49a 0%, rgba(63,164,154,0) 50%),
      linear-gradient(180deg, #7f8a6a 0%, #5d7d70 45%, #2a3a40 75%, var(--night) 100%);
  }
  .photo-credit {
    position: absolute; right: 14px; top: 22px;
    writing-mode: vertical-rl;
    font-size: 8px; color: #5a8fb0; letter-spacing: 0.2px;
  }
  .front-headline {
    position: absolute; left: 0; top: 342px; width: 548px; text-align: center;
    font-family: "Barlow Condensed", "Arial Narrow", sans-serif; font-weight: 700;
    font-size: 50px; line-height: 44px; color: var(--white); letter-spacing: 0.5px;
  }
  .front-headline .highlight { color: var(--salmon); }
  .front-copy {
    position: absolute; left: 49px; top: 496px; width: 280px;
    font-size: 16.5px; line-height: 19px; color: var(--white);
  }
  .front-copy p + p { margin-top: 19px; }
  .front-copy strong { font-weight: 700; }
  .front-callout {
    position: absolute; left: 47px; top: 710px; width: 370px;
    font-size: 14.5px; line-height: 19px; color: var(--lime-text);
  }
  .front-arrow { position: absolute; left: 370px; top: 712px; }

  .brand-mark { position: absolute; text-align: center; }
  .brand-mark .dot {
    display: block; margin: 0 auto; border-radius: 50%; background: var(--cyan);
  }
  .brand-mark .brand-name {
    display: block; font-family: "Rubik", Arial, sans-serif; font-weight: 700;
    color: var(--cyan); white-space: nowrap;
  }
  .front-brand { left: 350px; top: 530px; width: 164px; }
  .front-brand .dot { width: 66px; height: 66px; }
  .front-brand .brand-name { font-size: 34px; margin-top: 6px; }

  /* Back */
  .flyer-back {
    left: 611px; top: 107px; width: 547px; height: 774px; background: var(--white);
  }
  .back-intro {
    position: absolute; left: 0; top: 19px; width: 100%; text-align: center;
    font-size: 12.5px; color: var(--ink);
  }
  .price-block {
    position: absolute; left: 0; width: 100%; text-align: center;
    font-family: "Rubik", Arial, sans-serif;
  }
  .price-block .bin-type { font-weight: 700; font-size: 52px; line-height: 52px; }
  .price-block .first-clean { font-weight: 700; font-size: 33px; line-height: 36px; color: var(--ink); }
  .price-block .repeat-clean { font-weight: 300; font-size: 22px; line-height: 26px; color: var(--grey-text); }
  .price-dumpster { top: 50px; }
  .price-dumpster .bin-type { color: var(--cyan); }
  .price-wheelie { top: 224px; }
  .price-wheelie .bin-type { color: var(--lime); }

  .register-label {
    position: absolute; left: 30px; top: 400px; font-size: 14px; color: var(--lime-text);
  }
  .register-form {
    position: absolute; left: 0; top: 421px; width: 547px; height: 145px;
    background: var(--form-band); font-size: 14.5px; color: var(--lime-text);
  }
  .register-form .label { position: absolute; }
  .register-form .rule { position: absolute; height: 2px; background: var(--white); }
  .register-form .box { position: absolute; width: 73px; height: 21px; background: var(--field); }

  .text-us {
    position: absolute; left: 28px; top: 580px; color: var(--cyan);
  }
  .text-us .lead { font-size: 18.5px; line-height: 20px; }
  .text-us .number { font-size: 38px; line-height: 40px; font-weight: 300; }
  .example-tag { position: absolute; left: 40px; top: 645px; font-size: 11px; color: var(--ink); }
  .example-text {
    position: absolute; left: 28px; top: 667px;
    font-size: 20px; line-height: 22px; font-weight: 300; color: #444;
  }
  .back-brand { left: 342px; top: 600px; width: 170px; }
  .back-brand .dot { width: 70px; height: 70px; }
  .back-brand .brand-name { font-size: 36px; margin-top: 6px; }
</style>
</head>
<body>

<section class="flyer flyer-front">
  <div class="germ-photo" role="img" aria-label="Close-up photo of rod-shaped bacteria in orange and teal tones"></div>
  <span class="photo-credit">Image derived from photo of bacteria by Dario Menhall on PhotoShare</span>

  <h1 class="front-headline">CAREFUL, THIS BIN<br>MIGHT BE COVERED<br>IN <span class="highlight">HARMFUL</span> GERMS</h1>

  <div class="front-copy">
    <p>With germs everywhere you can’t underestimate the potential risks of cross-contamination.</p>
    <p>Your wheelie bins and dumpsters are an obvious place for germs to breed. <strong>Snapwell Mite Solutions</strong> are pleased to offer you a superb power washing service at an attractive price.</p>
  </div>

  <div class="brand-mark front-brand">
    <span class="dot"></span>
    <span class="brand-name">Snapwell</span>
  </div>

  <p class="front-callout">Whether you’re in the hotel and catering trade or a homeowner check out our great offers overleaf</p>
  <svg class="front-arrow" width="170" height="40" viewBox="0 0 170 40" aria-hidden="true">
    <path d="M4 32 C60 30 110 22 158 12" stroke="#ffffff" stroke-width="3" fill="none" stroke-linecap="round"/>
    <path d="M126 6 L160 11 L136 26" stroke="#ffffff" stroke-width="3" fill="none" stroke-linecap="round" stroke-linejoin="round"/>
  </svg>
</section>

<section class="flyer flyer-back">
  <p class="back-intro">Our crew will follow the waste disposal vehicle and clean your bin when empty</p>

  <div class="price-block price-dumpster">
    <div class="bin-type">4 wheeled<br>‘Dumpster’ bin</div>
    <div class="first-clean">£10 for the first clean</div>
    <div class="repeat-clean">(£5 per subsequent clean)</div>
  </div>

  <div class="price-block price-wheelie">
    <div class="bin-type">2 wheeled<br>‘Wheelie’ bin</div>
    <div class="first-clean">£6 for the first clean</div>
    <div class="repeat-clean">(£3 per subsequent clean)</div>
  </div>

  <p class="register-label">Register you details here:</p>
  <div class="register-form">
    <span class="label" style="left:30px; top:15px;">Name</span>
    <span class="rule" style="left:75px; top:31px; width:105px;"></span>
    <span class="label" style="left:188px; top:15px;">Address inc. postcode</span>
    <span class="rule" style="left:356px; top:31px; width:176px;"></span>
    <span class="rule" style="left:33px; top:56px; width:500px;"></span>
    <span class="label" style="left:30px; top:70px;">Tel.</span>
    <span class="rule" style="left:60px; top:86px; width:200px;"></span>
    <span class="label" style="left:280px; top:70px;">Bin(s)</span>
    <span class="label" style="left:336px; top:70px;">Wheelie</span>
    <span class="label" style="left:442px; top:70px;">Dumpster</span>
    <span class="label" style="left:242px; top:93px;">How many?</span>
    <span class="box" style="left:334px; top:92px;"></span>
    <span class="box" style="left:439px; top:92px;"></span>
    <span class="label" style="left:270px; top:118px;">Colour?</span>
    <span class="box" style="left:334px; top:118px;"></span>
    <span class="box" style="left:439px; top:118px;"></span>
  </div>

  <div class="text-us">
    <p class="lead">Or you can text your details to</p>
    <p class="number">07912 448731</p>
  </div>
  <span class="example-tag">eg</span>
  <p class="example-text">KT37QB, THE PUB<br>BLACK DUMPSTER<br>MONDAY SEPT 2014</p>

  <div class="brand-mark back-brand">
    <span class="dot"></span>
    <span class="brand-name">Snapwell</span>
  </div>
</section>

</body>
</html>
```